Permanent Holiday Lights - Yard Sign

This project aims to create a visually compelling yard sign that proudly represents the GlowCrest brand and draws attention in residential neighborhoods. The sign will serve as both a marketing tool and a badge of pride for customers who have chosen GlowCrest’ permanent lighting solutions. The design should capture GlowCrest’ premium, modern aesthetic while ensuring high visibility and readability from a distance.
Objectives:
Increase brand visibility in neighborhoods with GlowCrest installations.
Reinforce brand identity through consistent use of GlowCrest colors, logo, and typography.
Inspire curiosity and engagement, prompting passersby to visit the website or contact GlowCrest for more information.
Design Goals:
Use GlowCrest brand colors to ensure brand consistency and recognition.
Feature the GlowCrest logo prominently.
Include a clear, easy-to-read message — e.g.,

Does not require use of a home but am attaching pictures that could be used if the designer likes that.

Emphasize contrast and legibility, even at a distance or in various lighting conditions.
Incorporate a clean, modern design that reflects innovation and premium quality.
Deliverables:
Primary yard sign design (36”x24”, landscape orientation preferred)
Optional alternate versions for seasonal or promotional use
Print-ready files (CMYK, high-resolution PDF)
Digital mockups for presentation
Target Audience:
Homeowners and neighbors who value aesthetics, technology, and convenience—potential customers curious about GlowCrest when they see them in action.
Tone & Style:
Bright, confident, and contemporary
Reflects innovation, reliability, and lasting beauty
Clean and professional

Potential Tag Lines:
“We just added 4 billion colors to our home. Ask me about my new GlowCrest.”
“Our GlowCrest stays up. Our ladder stays down.”
“GlowCrest did this. (Arrow up) Come back at night to see what ‘this’ is.”

On the sign, please include either the website URL: www.myglowcrest-example.com OR the phone number: 555.417.8693

Target Market(s)

Middle to upper class (can be retired or have families) - interested in decor, having the nicest home in the block, and home improvements

Industry/Entity Type

Permanent Christmas Lights

Requirements
Must have
• On the sign, please include either the website URL: www.myglowcrest-example.com OR the phone number: 555.417.8693, A slogan /tag line like the ones I shared in the description. Captivating and colorful design.

```html
<!DOCTYPE html>
<html lang="en">
<head>
<meta charset="UTF-8">
<title>GlowCrest Yard Sign</title>
<link href="https://fonts.googleapis.com/css2?family=Montserrat:wght@500;600;800;900&display=swap" rel="stylesheet">
<style>
  :root {
    --bg: #f1f1ef;
    --white: #ffffff;
    --ink: #141414;
    --blue: #4169b2;
    --green: #7dc242;
    --yellow: #fbba1f;
    --teal: #43bd8f;
    --orange: #f4812f;
    --purple: #864b9b;
    --red: #ec2227;
    --pink: #ec3e96;
  }
  * { margin: 0; padding: 0; box-sizing: border-box; }
  html, body {
    width: 800px;
    height: 1200px;
    overflow: hidden;
    background: var(--bg);
    font-family: "Montserrat", sans-serif;
  }
  .yard-sign {
    position: absolute;
    left: 45px;
    top: 360px;
    width: 710px;
    height: 480px;
    background: var(--white);
    overflow: hidden;
    box-shadow: 0 14px 40px rgba(0,0,0,0.10);
  }
  .sign-backdrop {
    position: absolute;
    inset: 0;
    background:
      radial-gradient(ellipse 62% 58% at 50% 52%, var(--white) 55%, rgba(255,255,255,0) 100%),
      linear-gradient(90deg, #cfdaf0 0%, #dcefd0 30%, #fdebc2 55%, #fbd8c0 78%, #f8c9ca 100%);
  }
  .sign-copy {
    position: absolute;
    inset: 0;
    text-align: center;
  }
  .brand-name {
    position: absolute;
    top: 166px;
    left: 0;
    right: 0;
    display: flex;
    justify-content: center;
    align-items: center;
    gap: 14px;
    font-size: 31px;
    font-weight: 600;
    letter-spacing: 10px;
    color: var(--ink);
    line-height: 1;
  }
  .brand-dot {
    width: 14px;
    height: 14px;
    border-radius: 50%;
    background: var(--green);
  }
  .tagline-line {
    position: absolute;
    left: 0;
    right: 0;
    line-height: 1;
    white-space: nowrap;
  }
  .tagline-main {
    font-size: 45px;
    font-weight: 900;
    letter-spacing: -0.5px;
  }
  .tagline-sub {
    display: flex;
    justify-content: center;
    align-items: center;
    gap: 12px;
    font-size: 30px;
    font-weight: 600;
  }
  .tagline-sub::before,
  .tagline-sub::after {
    content: "";
    width: 26px;
    height: 9px;
    border-radius: 5px;
    background: currentColor;
  }
  .line-brand { top: 218px; color: var(--green); }
  .line-up { top: 264px; color: var(--orange); }
  .line-ladder { top: 294px; color: var(--blue); }
  .line-down { top: 338px; color: var(--pink); }
  .web-address {
    position: absolute;
    left: 150px;
    width: 410px;
    top: 390px;
    height: 44px;
    border-radius: 22px;
    background: var(--blue);
    color: var(--white);
    font-size: 21px;
    font-weight: 800;
    line-height: 44px;
    box-shadow: 0 14px 12px -8px rgba(0,0,0,0.22);
  }
</style>
</head>
<body>
  <main class="yard-sign">
    <div class="sign-backdrop" role="img" aria-label="Colourful rounded decorative shapes in blue, green, yellow, teal, orange, purple, red and pink around the sign edges"></div>

    <div class="sign-copy">
      <div class="brand-name"><span class="brand-dot"></span>GLOWCREST</div>
      <p class="tagline-line tagline-main line-brand">OUR GLOWCREST</p>
      <p class="tagline-line tagline-sub line-up">STAYS UP</p>
      <p class="tagline-line tagline-main line-ladder">OUR LADDER</p>
      <p class="tagline-line tagline-sub line-down">STAYS DOWN</p>
      <p class="web-address">www.myglowcrest-example.com</p>
    </div>
  </main>
</body>
</html>
```